Domestic Cleaning services needs a website

We need a descriptive, easy to use and trust inspiring website for domestic cleaning clients. It should be easy to use, with appointment scheduling and SMS notifiers. The brand name "BrightNest by Marguerite" should be associated with all offers at the website. blue/green/white colors should be more pronounced.
Website should be Mobile friendly.

Target Market(s)

Domestic Market. Long rental tourists, expats, local housewifes

Logo Text

BRIGHTNEST by MARGUERITE

Number of Pages Required

2 page

Font styles to use
Sans Serif

```html
<!DOCTYPE html>
<html lang="en">
<head>
<meta charset="utf-8">
<title>BrightNest by Marguerite — Domestic Cleaning</title>
<link rel="stylesheet" href="https://fonts.googleapis.com/css2?family=Raleway:wght@400;500;600&family=Roboto:wght@400;500&family=Roboto+Slab:wght@700&display=swap">
<style>
:root{
  --navy:#0b3a6b;
  --navy-dark:#082d54;
  --blue:#2d6aa3;
  --accent:#3f80bd;
  --text:#4a4a4a;
  --muted:#777;
  --light:#eeeeee;
  --white:#ffffff;
}
*{margin:0;padding:0;box-sizing:border-box}
html,body{width:1200px;height:3543px;overflow:hidden;background:var(--white)}
body{position:relative;font-family:'Roboto',sans-serif;color:var(--text)}
.abs{position:absolute}
.heading{font-family:'Raleway',sans-serif;font-weight:400;color:var(--navy);text-align:center;position:absolute;left:0;width:1200px}
.heading span{color:var(--accent)}
.btn{position:absolute;background:var(--navy);color:var(--white);font-family:'Roboto',sans-serif;font-size:19px;display:flex;align-items:center;justify-content:center;border-radius:3px;text-transform:uppercase}
.photo{position:absolute}

/* header */
.brand{left:78px;top:40px;display:flex;align-items:center;gap:14px;font-family:'Raleway',sans-serif;font-weight:600;font-size:27px;color:var(--navy)}
.brand-dot{width:34px;height:34px;border-radius:50%;background:var(--navy)}
.help{right:78px;top:12px;font-size:20px;color:var(--navy);display:flex;align-items:center;gap:10px;font-weight:500}
.social{width:48px;height:48px;border-radius:50%;background:var(--blue);position:absolute}
.account{left:957px;top:111px;width:165px;height:35px;background:#8f9499;color:var(--white);font-size:15px;display:flex;align-items:center;justify-content:center;gap:10px}
.nav{left:0;top:158px;width:1200px;height:59px;background:var(--navy)}
.nav a{position:absolute;top:0;height:59px;line-height:59px;color:var(--white);text-decoration:none;font-size:19px;font-weight:500}
.nav .active{background:var(--blue);width:135px;text-align:center;left:78px}

/* hero */
.hero{left:0;top:217px;width:1200px;height:617px;background:linear-gradient(90deg,#c9c6c2 0%,#e7e4e0 35%,#f3f3f1 60%,#e6e6e2 100%)}
.hero-title{left:78px;top:365px;font-family:'Roboto Slab',serif;font-weight:700;font-size:48px;line-height:56px;color:var(--navy)}
.hero-title .b{color:var(--blue)}
.hero-text{left:78px;top:486px;width:330px;font-size:17px;line-height:24px;color:#555}

/* welcome */
.welcome-text{left:177px;top:966px;width:846px;text-align:center;font-size:16px;line-height:25px;color:#555}
.rule{height:2px;background:var(--navy)}

/* about */
.about{left:0;top:1138px;width:1200px;height:426px;background:var(--light)}
.about-title{position:absolute;right:669px;top:1310px;font-family:'Raleway',sans-serif;font-weight:500;font-size:26px;color:var(--blue)}
.about-text{right:669px;top:1350px;width:420px;text-align:right;font-size:16px;line-height:25px;color:#666}
.more{font-size:19px;color:var(--navy);font-weight:500;display:flex;align-items:center;gap:12px}

/* domestic */
.card{position:absolute;top:1684px;width:239px;height:362px;border:2px solid #ddd;background:var(--white);text-align:center}
.card .photo{left:0;top:0;width:235px;height:166px;position:absolute}
.card h4{position:absolute;top:180px;left:0;width:100%;font-weight:500;font-size:21px;color:var(--navy)}
.card p{position:absolute;top:220px;left:30px;width:175px;font-size:16px;line-height:24px;color:#777}
.card .btn{top:303px;left:56px;width:123px;height:42px;font-size:17px}

/* commercial */
.commercial{left:0;top:2098px;width:1200px;height:500px;background:linear-gradient(180deg,#4a3b33 0%,#5a4a3f 50%,#3c302a 100%)}
.ring{position:absolute;width:151px;height:151px;border-radius:50%;border:4px solid var(--white)}
.svc{position:absolute;color:var(--white);width:165px}
.svc h5{font-weight:500;font-size:21px;margin-bottom:10px}
.svc p{font-size:15px;line-height:23px;color:#eee}
.r{text-align:right}
.arch{left:432px;top:2480px;width:331px;height:236px;border-radius:50%;background:var(--white)}

/* news */
.sub-title{position:absolute;font-family:'Raleway',sans-serif;font-weight:400;font-size:32px;color:var(--navy);text-align:center;width:560px}
.sub-title span{color:var(--accent)}
.news-item h6{position:absolute;font-size:17px;font-weight:500;color:var(--navy)}
.news-date{position:absolute;font-size:13px;color:var(--muted)}
.news-text{position:absolute;font-size:15px;line-height:22px;color:#666;width:310px}
.small-more{position:absolute;font-size:14px;color:var(--blue);display:flex;align-items:center;gap:10px}

/* newsletter */
.news-bg{left:0;top:3035px;width:1200px;height:307px;background:linear-gradient(90deg,#e9ecee,#f8f9fa 50%,#e9ecee)}
.input{left:300px;top:3226px;width:416px;height:55px;border:1px solid #bbb;background:#f2f2f2;font-size:15px;color:#777;padding-left:16px;display:flex;align-items:center}
.subscribe{left:727px;top:3225px;width:175px;height:57px;border-radius:29px;background:var(--navy);color:var(--white);font-family:'Roboto Slab',serif;font-weight:700;font-size:21px;display:flex;align-items:center;justify-content:center;letter-spacing:1px}

/* footer */
.footer{left:0;top:3342px;width:1200px;height:201px;background:var(--navy)}
.flink{position:absolute;top:3375px;color:var(--white);font-size:18px}
.fsoc{position:absolute;width:52px;height:52px;border-radius:50%;border:2px solid var(--white)}
.ficon{position:absolute;width:46px;height:46px;border-radius:50%;background:var(--white);display:flex;align-items:center;justify-content:center}
.ftext{position:absolute;color:var(--white);font-size:15px;line-height:21px}
</style>
</head>
<body>

<!-- header -->
<div class="abs brand"><div class="brand-dot"></div>BRIGHTNEST by MARGUERITE</div>
<div class="abs help">How can we help
  <svg width="24" height="24" viewBox="0 0 24 24"><path fill="#0b3a6b" d="M6.6 10.8c1.4 2.8 3.8 5.1 6.6 6.6l2.2-2.2c.3-.3.7-.4 1-.2 1.1.4 2.3.6 3.6.6.6 0 1 .4 1 1V20c0 .6-.4 1-1 1C10.6 21 3 13.4 3 4c0-.6.4-1 1-1h3.5c.6 0 1 .4 1 1 0 1.3.2 2.5.6 3.6.1.3 0 .7-.2 1z"/></svg>
  555-210-4821</div>
<div class="social" style="left:911px;top:49px" role="img" aria-label="Social profile"></div>
<div class="social" style="left:992px;top:49px" role="img" aria-label="Social profile"></div>
<div class="social" style="left:1074px;top:49px" role="img" aria-label="Social profile"></div>
<div class="abs account"><span>LOG IN</span><span>|</span><span>SIGN UP</span></div>

<nav class="abs nav">
  <a class="active" href="#">HOME</a>
  <a href="#" style="left:283px">ABOUT</a>
  <a href="#" style="left:418px">SERVICES</a>
  <a href="#" style="left:579px">CONTACT</a>
</nav>

<!-- hero -->
<div class="photo hero" role="img" aria-label="Bright bedroom with a smiling cleaner holding a bucket of cleaning supplies"></div>
<div class="abs hero-title">BrightNest<br><span class="b">by Marguerite</span></div>
<p class="abs hero-text">Lorem Ipsum is simply dummy text of the printing and typesetting industry.</p>
<div class="btn" style="left:78px;top:581px;width:260px;height:59px;font-size:21px">Read More</div>

<!-- welcome -->
<h2 class="heading" style="top:880px;font-size:42px">Welcome to <span>BrightNest by Marguerite</span></h2>
<div class="abs rule" style="left:524px;top:946px;width:152px"></div>
<p class="abs welcome-text">Lorem Ipsum is simply dummy text of the printing and typesetting industry. Lorem Ipsum has been the industry's standard dummy text ever since the 1500s, when an unknown printer took a galley of type and scrambled it to make a type specimen book.</p>
<svg class="abs" style="left:582px;top:1058px" width="36" height="34" viewBox="0 0 36 34"><path d="M4 4l14 12 14-12M4 18l14 12 14-12" fill="none" stroke="#444" stroke-width="3"/></svg>

<!-- about -->
<section class="abs about"></section>
<h2 class="heading" style="top:1163px;font-size:42px">About <span>Us</span></h2>
<p class="abs" style="left:0;width:1200px;top:1218px;text-align:center;font-size:16px;color:#555">Lorem Ipsum is simply dummy text of the printing and typesetting industry.</p>
<h3 class="about-title">How to Work Us.....</h3>
<p class="abs about-text">Lorem Ipsum is simply dummy text of the printing and typesetting industry. Lorem Ipsum has been the industry's standard dummy text ever since the 1500s.</p>
<div class="abs more" style="right:669px;top:1443px">READ MORE
  <svg width="16" height="14" viewBox="0 0 16 14"><path d="M2 2l5 5-5 5M9 2l5 5-5 5" fill="none" stroke="#0b3a6b" stroke-width="2"/></svg></div>
<div class="abs" style="left:588px;top:1276px;width:447px;height:236px;background:var(--white);padding:10px">
  <div class="photo" style="position:relative;width:100%;height:100%;background:linear-gradient(90deg,#a56a3a,#d8cfc4 55%,#cfd6de)" role="img" aria-label="Two cleaners in blue aprons smiling in a tidy room"></div>
</div>

<!-- domestic services -->
<h2 class="heading" style="top:1612px;font-size:42px">Our Domestic <span>Services</span></h2>
<div class="card" style="left:78px">
  <div class="photo" style="background:linear-gradient(135deg,#d9d4cc,#b7a89a)" role="img" aria-label="Cleaner with a trolley cleaning carpet"></div>
  <h4>Carpet Cleaning</h4><p>Lorem Ipsum is simply dummy text of the printing typesetting</p><div class="btn">Read More</div>
</div>
<div class="card" style="left:347px">
  <div class="photo" style="background:linear-gradient(135deg,#cfe0dc,#9fb7c4)" role="img" aria-label="Woman ironing folded laundry"></div>
  <h4>Ironing</h4><p>Lorem Ipsum is simply dummy text of the printing typesetting</p><div class="btn">Read More</div>
</div>
<div class="card" style="left:616px">
  <div class="photo" style="background:linear-gradient(180deg,#e4e2df,#8e8a86)" role="img" aria-label="Steam cleaning a tiled floor"></div>
  <h4>Tiled floor steam clean</h4><p>Lorem Ipsum is simply dummy text of the printing typesetting</p><div class="btn">Read More</div>
</div>
<div class="card" style="left:883px">
  <div class="photo" style="background:linear-gradient(135deg,#e8e4dc,#b98a5c)" role="img" aria-label="Empty room with moving boxes and a cleaner"></div>
  <h4>End of tenancy clean</h4><p>Lorem Ipsum is simply dummy text of the printing typesetting</p><div class="btn">Read More</div>
</div>

<!-- commercial services -->
<section class="abs commercial" role="img" aria-label="Dim background of a hand wiping a surface"></section>
<h2 class="heading" style="top:2128px;font-size:42px;color:var(--white)"><span>Our Commercial</span> Services</h2>
<div class="ring photo" style="left:391px;top:2205px;background:linear-gradient(135deg,#e9e36a,#8a8a8a)" role="img" aria-label="Worker in a high-visibility suit polishing a desk"></div>
<div class="svc r" style="left:208px;top:2222px"><h5>Desk polishing</h5><p>Lorem Ipsum is simply dummy text of the printing type setting</p></div>
<div class="ring photo" style="left:643px;top:2211px;background:linear-gradient(135deg,#d8d8d8,#7d8a98)" role="img" aria-label="Cleaner emptying office bins"></div>
<div class="svc" style="left:817px;top:2222px"><h5>Bin emptying</h5><p>Lorem Ipsum is simply dummy text of the printing type setting</p></div>
<div class="ring photo" style="left:244px;top:2398px;background:linear-gradient(135deg,#e6e1d8,#c9b23a)" role="img" aria-label="Woman vacuuming a floor"></div>
<div class="svc r" style="left:72px;top:2413px"><h5>Vacuuming</h5><p>Lorem Ipsum is simply dummy text of the printing type setting</p></div>
<div class="ring photo" style="left:794px;top:2398px;background:linear-gradient(135deg,#e8e8e8,#3a3a3a)" role="img" aria-label="Cleaner in uniform cleaning a toilet"></div>
<div class="svc" style="left:968px;top:2413px"><h5>Toilet cleaning</h5><p>Lorem Ipsum is simply dummy text of the printing type setting</p></div>
<div class="abs arch" style="clip-path:inset(0 0 118px 0)"></div>
<div class="abs" style="left:432px;top:2518px;width:331px;display:flex;justify-content:center;align-items:center;gap:8px;font-family:'Raleway',sans-serif;font-weight:600;font-size:15px;color:var(--navy)"><div style="width:16px;height:16px;border-radius:50%;background:var(--navy)"></div>BRIGHTNEST by MARGUERITE</div>

<!-- latest news -->
<h3 class="sub-title" style="left:44px;top:2648px">LATEST <span>NEWS</span></h3>
<div class="abs" style="left:602px;top:2670px;width:1px;height:330px;background:#ccc"></div>
<div class="news-item">
  <div class="photo" style="left:144px;top:2716px;width:116px;height:85px;background:linear-gradient(135deg,#e4d6c8,#b55b4a)" role="img" aria-label="Cleaners at work in a kitchen"></div>
  <h6 style="left:274px;top:2713px">Lorem Ipsum is simply dummy text</h6>
  <div class="news-date" style="left:274px;top:2740px">&#9638; 10 JULY 2016</div>
  <p class="news-text" style="left:274px;top:2760px">Lorem Ipsum is simply dummy text of the printing and typesetting industry.......</p>
  <div class="small-more" style="left:274px;top:2812px">READ MORE <span>&#187;</span></div>
</div>
<div class="abs" style="left:144px;top:2845px;width:406px;height:1px;background:#ddd"></div>
<div class="news-item">
  <div class="photo" style="left:144px;top:2876px;width:116px;height:85px;background:linear-gradient(135deg,#d6c3a8,#3f6fa6)" role="img" aria-label="Two cleaners in blue aprons"></div>
  <h6 style="left:274px;top:2873px">Lorem Ipsum is simply dummy text</h6>
  <div class="news-date" style="left:274px;top:2900px">&#9638; 10 JULY 2016</div>
  <p class="news-text" style="left:274px;top:2920px">Lorem Ipsum is simply dummy text of the printing and typesetting industry.......</p>
  <div class="small-more" style="left:274px;top:2972px">READ MORE <span>&#187;</span></div>
</div>

<!-- testimonial -->
<h3 class="sub-title" style="left:577px;top:2648px">CLIENT <span>TESTIMONIAL</span></h3>
<p class="abs" style="left:722px;top:2706px;width:280px;text-align:center;font-size:15px;line-height:23px;color:#666">Lorem Ipsum is simply dummy text of the printing and typesetting industry. Lorem Ipsum has been the industry's</p>
<div class="photo" style="left:796px;top:2802px;width:132px;height:132px;border-radius:50%;border:3px solid #ddd;background:linear-gradient(135deg,#cfe0ee,#8fb0cc)" role="img" aria-label="Client portrait"></div>
<p class="abs" style="left:712px;top:2948px;width:300px;text-align:center;font-size:15px;color:var(--navy);font-weight:500">- DANA WHITFIELD</p>

<!-- newsletter -->
<section class="abs news-bg" role="img" aria-label="Soft-focus bright interior with a seated figure"></section>
<h2 class="heading" style="top:3055px;font-size:44px;color:#111">NEWSLETTER</h2>
<p class="abs" style="left:0;width:1200px;top:3134px;text-align:center;font-size:19px;color:#222">Get our daily news delivered to your email</p>
<div class="abs input">Your E-Mail</div>
<div class="abs subscribe">SUBSCRIBE</div>

<!-- footer -->
<footer class="abs footer"></footer>
<div class="flink" style="left:80px">Home</div>
<div class="flink" style="left:172px">About</div>
<div class="flink" style="left:267px">Services</div>
<div class="flink" style="left:376px">Contact</div>
<div class="abs" style="left:718px;top:3367px;width:163px;height:36px;background:var(--blue);color:var(--white);font-size:15px;display:flex;align-items:center;justify-content:center;gap:10px"><span>LOG IN</span><span>|</span><span>SIGN UP</span></div>
<div class="fsoc" style="left:916px;top:3359px" role="img" aria-label="Social profile"></div>
<div class="fsoc" style="left:994px;top:3359px" role="img" aria-label="Social profile"></div>
<div class="fsoc" style="left:1070px;top:3359px" role="img" aria-label="Social profile"></div>
<div class="abs" style="left:78px;top:3439px;width:1044px;height:1px;background:rgba(255,255,255,.5)"></div>

<div class="ficon" style="left:76px;top:3458px"><svg width="20" height="24" viewBox="0 0 20 24"><path fill="#0b3a6b" d="M10 0a8 8 0 0 0-8 8c0 6 8 16 8 16s8-10 8-16a8 8 0 0 0-8-8zm0 11a3 3 0 1 1 0-6 3 3 0 0 1 0 6z"/></svg></div>
<p class="ftext" style="left:130px;top:3451px;width:160px">Lorem Ipsum is simply dummy text of the printing.</p>
<div class="ficon" style="left:348px;top:3458px"><svg width="22" height="22" viewBox="0 0 24 24"><path fill="#0b3a6b" d="M6.6 10.8c1.4 2.8 3.8 5.1 6.6 6.6l2.2-2.2c.3-.3.7-.4 1-.2 1.1.4 2.3.6 3.6.6.6 0 1 .4 1 1V20c0 .6-.4 1-1 1C10.6 21 3 13.4 3 4c0-.6.4-1 1-1h3.5c.6 0 1 .4 1 1 0 1.3.2 2.5.6 3.6.1.3 0 .7-.2 1z"/></svg></div>
<p class="ftext" style="left:406px;top:3471px">555 318 2046</p>
<div class="ficon" style="left:619px;top:3458px"><svg width="22" height="16" viewBox="0 0 22 16"><rect x="1" y="1" width="20" height="14" rx="2" fill="none" stroke="#0b3a6b" stroke-width="2"/><path d="M1 2l10 7 10-7" fill="none" stroke="#0b3a6b" stroke-width="2"/></svg></div>
<p class="ftext" style="left:676px;top:3471px">hello@brightnestcleaning.com</p>
<p class="ftext" style="left:973px;top:3461px">© <b>BRIGHTNEST</b> 2017.<br>All Rights Reserved.</p>

</body>
</html>
```